Flyer-Design für Linkshänder-Versandhandel
Zielgruppe
Online Versandhandel für Linkshänderprodukte
Aufgabenstellung
- Blau und Grüntöne mit passenden Ergänzungen
- Der Flyer soll ein 6-seitiger Wickelfalz sein
- Innen sollte Platz für Text sein

```html
<!DOCTYPE html>
<html lang="de">
<head>
<meta charset="utf-8">
<title>Tauschwerk – Wickelfalz-Flyer</title>
<link href="https://fonts.googleapis.com/css2?family=Archivo:wght@400;600;700;800&family=Mrs+Saint+Delafield&display=swap" rel="stylesheet">
<style>
  :root{
    --bg:#ececec;
    --paper:#f7f7f7;
    --grey-dark:#c4c4c4;
    --grey-mid:#cdcdcd;
    --grey-light:#dddddd;
    --grey-text:#6d6d6d;
    --grey-head:#e0e0e0;
    --placeholder:#e2e2e2;
    --green:#aabd52;
    --green-bright:#b3c560;
    --olive:#8a9b3d;
    --blue:#3aa3d6;
    --blue-title:#2a8bc5;
    --white:#ffffff;
  }
  *{box-sizing:border-box;margin:0;padding:0}
  html,body{width:1200px;height:900px;overflow:hidden}
  body{background:var(--bg);font-family:"Archivo",Arial,sans-serif;color:var(--grey-text);position:relative}

  .spread{position:absolute;top:244px;width:570px;height:412px;display:flex;box-shadow:0 6px 18px rgba(0,0,0,.12)}
  .spread--outside{left:22px}
  .spread--inside{left:608px}
  .panel{position:relative;width:190px;height:412px;overflow:hidden;background:var(--paper)}
  .panel--cover{background:var(--grey-dark)}
  .panel--quote{background:var(--grey-mid)}
  .panel--shop{background:var(--grey-light)}

  .abs{position:absolute}
  .kicker{font-weight:700;font-size:10px;line-height:1;text-transform:uppercase}
  .headline{font-weight:800;font-size:16px;line-height:1;text-transform:uppercase}
  .green{color:var(--green)}
  .blue{color:var(--blue-title)}
  .body{font-size:5.6px;line-height:7.8px;color:var(--grey-text)}
  .label{font-weight:700;font-size:5.2px;line-height:1;text-transform:uppercase}

  /* panel: Das machen wir */
  .image-slot{left:17px;top:106px;width:153px;height:88px;background:var(--placeholder)}
  .feature{top:324px;width:40px;text-align:center}
  .feature__dot{width:27px;height:27px;border-radius:50%;background:var(--green);margin:0 auto 8px}

  /* panel: Wir sind auch */
  .contact-band{left:0;bottom:0;width:190px;height:112px;background:var(--blue)}

  /* cover */
  .brand{left:22px;top:34px;display:flex;align-items:center;gap:6px;z-index:2}
  .brand__dot{width:20px;height:20px;border-radius:50%;background:var(--green)}
  .brand__name{font-weight:800;font-size:13px;color:var(--blue-title);letter-spacing:.2px}
  .cover-circle{left:16px;top:105px;width:178px;height:178px;border-radius:50%;background:var(--blue)}
  .portrait{left:70px;top:78px;width:120px;height:236px;border-radius:50px 50px 0 0;
    background:linear-gradient(180deg,rgba(200,200,200,.85),rgba(176,176,176,.9))}
  .cover-band{left:0;bottom:0;width:190px;height:112px;background:var(--olive);
    clip-path:polygon(0 0,100% 22%,100% 100%,0 100%)}
  .cover-text{left:24px;top:325px}
  .tiny{font-size:4.5px;font-weight:600;color:var(--grey-head)}
  .quote-small{font-weight:700;font-size:14px;line-height:1;color:var(--grey-head);margin-top:4px}
  .quote-big{font-weight:800;font-size:26px;line-height:1;color:var(--grey-head)}
  .signature{font-family:"Mrs Saint Delafield",cursive;font-size:15px;line-height:1;color:var(--grey-head);opacity:.75}

  /* inside: quote panel */
  .blob{left:-70px;top:62px;width:290px;height:270px;border-radius:50%;background:var(--green)}
  .portrait-wide{left:104px;top:92px;width:86px;height:250px;border-radius:60px 0 0 40px;
    background:linear-gradient(160deg,rgba(215,215,215,.75),rgba(190,190,190,.6))}
  .big-quote{left:19px;top:94px;font-weight:800;font-size:22px;line-height:23.5px;color:var(--grey-head);text-transform:uppercase;z-index:2}
  .quote-sign{left:12px;top:237px;z-index:2}

  /* inside: shop panel */
  .shop-copy{left:28px;top:97px;width:136px;text-align:center}
  .offer{left:57px;top:278px;width:120px;height:110px;background:var(--green-bright);padding:10px 10px}
  .offer__title{font-weight:700;font-size:10px;line-height:10px;color:var(--grey-head);text-transform:uppercase}
  .offer__copy{position:absolute;left:10px;bottom:9px;width:100px;font-size:5.6px;line-height:7.6px;color:var(--grey-head)}
  .price{left:128px;top:248px;width:40px;height:40px;border-radius:50%;background:var(--blue);
    color:var(--white);font-weight:700;font-size:9px;display:flex;align-items:center;justify-content:center}

  /* list panel */
  .list-item{left:18px;display:flex;gap:12px;align-items:center;width:165px}
  .list-item__dot{flex:none;width:42px;height:42px;border-radius:50%;background:var(--placeholder)}
  .list-item__title{font-weight:700;font-size:5.2px;color:var(--blue-title);text-transform:uppercase;margin-bottom:1.5px}
  .closing{left:18px;top:333px;width:160px}
</style>
</head>
<body>

<!-- Außenseite -->
<section class="spread spread--outside">
  <article class="panel">
    <p class="abs kicker green" style="left:17px;top:70px">Das machen wir</p>
    <h2 class="abs headline green" style="left:17px;top:82px">Mit Links</h2>
    <div class="abs image-slot" role="img" aria-label="Bildfläche für Produktfoto"></div>
    <p class="abs label green" style="left:17px;top:212px">Unser Unternehmen</p>
    <p class="abs body" style="left:17px;top:219px;width:150px">fugia dem quam, es ut veri ni blaut es aut aliquibus am id quas apiet et aliam que conserum volorem exeribus rehendi tatempel ium volorehent.Lique dolum aliquate num rehenisti velende bisqui que conserum volorem exeribus rehendi tatempel ium volorehent.Lique dolum aliquate num rehenisti velende bisqui que conserum</p>
    <p class="abs body" style="left:17px;top:282px;width:150px">volorem exeribus rehendi tatempel ium volorehent.Lique dolum aliquate num rehenisti velend aliquate num rehenisti velende bisqui que conserum volorem exeribus re</p>
    <div class="abs feature" style="left:16px"><div class="feature__dot"></div><p class="label green">Videndit</p></div>
    <div class="abs feature" style="left:70px"><div class="feature__dot"></div><p class="label green">Videndit</p></div>
    <div class="abs feature" style="left:124px"><div class="feature__dot"></div><p class="label green">Videndit</p></div>
  </article>

  <article class="panel">
    <p class="abs kicker blue" style="left:18px;top:62px">Wir sind auch</p>
    <h2 class="abs headline blue" style="left:18px;top:74px;font-size:17px">Ver(link)t.</h2>
    <p class="abs body" style="left:18px;top:104px;width:160px">Ga. Ut la sum ni cum videndit fugia dem quam, es ut veri ni blaut es aut aliquibus am id quas apiet et aliam que conserum volorem exeribus rehendi tatempel ium volorehent.Lique dolum aliquate num rehenisti velende bisqui</p>
    <h3 class="abs kicker blue" style="left:18px;top:187px;font-size:11px">Kontakt</h3>
    <p class="abs body" style="left:18px;top:206px;width:135px">Ga. Ut la sum ni cum videndit fugia dem quam, es ut veri ni blaut es aut aliquibus am id quas apiet et aliam que conserum volorem exe</p>
    <p class="abs body" style="left:18px;top:244px;width:135px">Ga. Ut la sum ni cum videndit fugia dem quam, es ut veri ni blaut es aut aliquibus am id quas apiet et aliam que conserum volorem exe</p>
    <div class="abs contact-band"></div>
  </article>

  <article class="panel panel--cover">
    <div class="abs brand"><span class="brand__dot"></span><span class="brand__name">TAUSCHWERK</span></div>
    <div class="abs cover-circle"></div>
    <div class="abs portrait" role="img" aria-label="Strichzeichnung eines berühmten Linkshänders mit erhobenem Daumen"></div>
    <div class="abs cover-band"></div>
    <div class="abs cover-text">
      <p class="tiny">Berühmeter Linkshänder</p>
      <p class="quote-small">ERSCHAFFE</p>
      <p class="quote-big">MIT LINKS</p>
      <p class="signature">Lorenzo Valmonte</p>
    </div>
  </article>
</section>

<!-- Innenseite -->
<section class="spread spread--inside">
  <article class="panel panel--quote">
    <div class="abs blob"></div>
    <div class="abs portrait-wide" role="img" aria-label="Strichzeichnung einer berühmten Linkshänderin"></div>
    <p class="abs big-quote">Links<br>ist<br>meine<br>Schoko<br>laden<br>Seite</p>
    <div class="abs quote-sign">
      <p class="signature" style="font-size:14px">Mira Solvay</p>
      <p class="tiny" style="margin-left:7px;margin-top:1px">Berühmte Linkshänderin</p>
    </div>
  </article>

  <article class="panel panel--shop">
    <p class="abs kicker blue" style="left:18px;top:66px">Das kaufe ich</p>
    <h2 class="abs headline blue" style="left:18px;top:78px">Mit Links</h2>
    <div class="abs shop-copy body">
      <p>Ga. Ut la sum ni cum videndit fugia dem quam, es ut veri ni blaut es aut aliquibus am id quas apiet et aliam que conserum volorem exeribus rehendi tatempel ium volorehent.Lique dolum aliquate num rehenisti velende bisqui Ga.</p>
      <p style="margin-top:5px">Ut la sum ni cum videndit fugia dem quam, es ut veri ni blaut es aut aliquibus am id quas apiet et aliam que conserum volorem exeribus rehendi tatempel ium volorehent.Lique dolum aliquate num</p>
      <p class="label blue" style="margin-top:8px">Rehenisti velende bisqui</p>
    </div>
    <div class="abs offer">
      <p class="offer__title">Angebot<br>des Monats</p>
      <p class="offer__copy">videndit fugia dem quam, es ut veri et aliam que conserum volorem exeribus rehendi</p>
    </div>
    <div class="abs price">€ XX.-</div>
  </article>

  <article class="panel">
    <div class="abs list-item" style="top:51px"><span class="list-item__dot"></span><div><p class="list-item__title">Ga. Ut la sum</p><p class="body">ni cum videndit fugia dem quam, es ut veri et aliam que conserum bisqui</p></div></div>
    <div class="abs list-item" style="top:105px"><span class="list-item__dot"></span><div><p class="list-item__title">Ga. Ut la sum ni cum videndit fugia</p><p class="body">dem quam, es ut veri et aliam que conserum volorem exeribus rehendi tatempel</p></div></div>
    <div class="abs list-item" style="top:159px"><span class="list-item__dot"></span><div><p class="list-item__title">Ga. Ut la sum n</p><p class="body">cum videndit fugia dem quam, es ut veri et aliam que conserum volorem exeribus rehendi tatempel ium</p></div></div>
    <div class="abs list-item" style="top:213px"><span class="list-item__dot"></span><div><p class="list-item__title">Ga. Ut la sum ni cum</p><p class="body">videndit fugia dem quam, es ut veri et aliam que conserum volorem exeribus rehendi tatempel ium volorehent.</p></div></div>
    <div class="abs list-item" style="top:266px"><span class="list-item__dot"></span><div><p class="list-item__title">Ga. Ut la sum ni</p><p class="body">cum videndit fugia dem quam, es ut veri et aliam que conserum volorem exeribus rehendqui</p></div></div>
    <div class="abs closing">
      <p class="list-item__title">Ga. Ut la sum ni cum videndit</p>
      <p class="body">fugia dem quam, es ut veri ni blaut es aut aliquibus am id quas apiet et aliam que conserum volorem exeribus rehendi tatempel ium volorehent.Lique dolum aliquate num rehenisti velende bisqui</p>
    </div>
  </article>
</section>

</body>
</html>
```